Security Business card

I need a new business card for my new company Bastion Crest Security Group we provide security for clubs,pubs,hotels etc. I would like to see the main colors red and black to be used. The final design should communicate honor and integrity.

Industry/Entity Type

Security

Contact Information for Business Card

Marcus Delvane
Company Name-Bastion Crest Security Group
Abn-47318265094
Acn-318265094
address- po box 7352 Ferndale nsw 2291
phone- 0437682915
email- Marcus@bastioncrest.com.au

```html
<!DOCTYPE html>
<html lang="en">
<head>
<meta charset="utf-8">
<title>Bastion Crest Security Group – Business Card</title>
<link rel="stylesheet" href="https://fonts.googleapis.com/css2?family=Arimo:wght@400&display=swap">
<style>
  :root {
    --brand-red: #e8141c;
    --deep-red: #7a0000;
    --bright-red: #d61010;
    --ink: #333333;
    --muted: #555555;
    --divider: #8a8f8f;
    --top-bar: #0b0b0b;
    --paper: #ffffff;
    --card-font: "Arimo", Arial, sans-serif;
  }
  * { margin: 0; padding: 0; box-sizing: border-box; }
  html, body {
    width: 1200px; height: 720px; overflow: hidden; background: var(--paper);
  }
  .card {
    position: relative; width: 1200px; height: 720px; overflow: hidden;
    background: var(--paper); font-family: var(--card-font);
  }
  .top-bar {
    position: absolute; top: 0; left: 0; width: 100%; height: 21px;
    background: var(--top-bar);
  }
  .base-waves {
    position: absolute; left: 0; top: 0; width: 1200px; height: 720px;
  }
  .brand-mark {
    position: absolute; left: 223px; top: 191px; width: 136px; height: 136px;
    border-radius: 50%; background: var(--brand-red);
  }
  .company-name {
    position: absolute; left: 33px; width: 560px; top: 368px;
    text-align: center; color: var(--brand-red);
    font-size: 43px; font-weight: 400; line-height: 53px;
  }
  .divider {
    position: absolute; left: 620px; top: 165px; width: 2px; height: 310px;
    background: var(--divider);
  }
  .person-name {
    position: absolute; left: 717px; top: 203px;
    color: var(--brand-red); font-size: 33px; font-weight: 400;
  }
  .person-role {
    position: absolute; left: 776px; top: 243px;
    color: var(--muted); font-size: 19px;
  }
  .contact-list {
    position: absolute; left: 717px; top: 343px; list-style: none;
    color: var(--ink); font-size: 20.5px; line-height: 35.5px;
  }
  .registration {
    position: absolute; top: 660px; color: var(--paper); font-size: 23px;
  }
  .registration.abn { left: 298px; }
  .registration.acn { left: 682px; }
</style>
</head>
<body>
<main class="card">
  <div class="top-bar"></div>

  <svg class="base-waves" viewBox="0 0 1125 675" preserveAspectRatio="none" aria-hidden="true">
    <defs>
      <linearGradient id="redBand" x1="0" y1="0" x2="0" y2="1">
        <stop offset="0" stop-color="#7a0000"/>
        <stop offset="1" stop-color="#d61010"/>
      </linearGradient>
      <linearGradient id="leftSwoosh" x1="0" y1="0" x2="1" y2="0">
        <stop offset="0" stop-color="#6f7474"/>
        <stop offset="0.5" stop-color="#1e1e1e"/>
        <stop offset="1" stop-color="#111111"/>
      </linearGradient>
      <linearGradient id="rightSwoosh" x1="0" y1="0" x2="1" y2="0">
        <stop offset="0" stop-color="#111111"/>
        <stop offset="0.6" stop-color="#2b2e2e"/>
        <stop offset="1" stop-color="#6a7070"/>
      </linearGradient>
    </defs>
    <path d="M0,505 C150,545 350,562 560,563 C350,576 150,566 0,537 Z" fill="url(#leftSwoosh)"/>
    <path d="M720,548 C900,528 1030,488 1125,440 L1125,472 C1030,508 900,538 720,548 Z" fill="url(#rightSwoosh)"/>
    <path d="M0,555 C250,600 560,602 800,562 C950,537 1060,512 1125,495 L1125,675 L0,675 Z" fill="url(#redBand)"/>
  </svg>

  <div class="brand-mark"></div>
  <h1 class="company-name">Bastion Crest Security<br>Group</h1>

  <div class="divider"></div>

  <h2 class="person-name">Marcus Delvane</h2>
  <p class="person-role">(Lorem Ispom)</p>

  <ul class="contact-list">
    <li>Ph.:- 0437 682 915</li>
    <li>Email:- Marcus@bastioncrest.com.au</li>
    <li>Address:- Po box 7352 Ferndale nsw 2291</li>
  </ul>

  <p class="registration abn">Abn-47318265094</p>
  <p class="registration acn">Acn-318265094</p>
</main>
</body>
</html>
```